Personal Training Studio Checkin App (or URL based)

I would like a simple web based app built for our  business. We have a training studio with a simple business model. All our clients buy sessions in packages either 4, 8, or 12 at a time. We want something that a trainer can pull up and Check in a client. This will record the date and time the client was checked in, by what trainer, and what type of session. This system will keep track of the following:
Whenever a Client Checks in so it will ‘tick off’ a session on their package (ie- they have gone from 11 sessions left to 10 sessions left)
Track what sessions a particular trainer does so we can pay them at the end of the week and look at who they trained, what type of session and how many
Look at client activity: Every time they check in, Recharge their package, any activity related to the client, even if it was admin – like deleting a session that was mistakenly recorded.
This will keep a database of clients added and all their activity
The pdf I have included lays out how I think it would work and the features I want
I would like this to run off an vornix that we have at our front check in counter. It can be an app or a URL that use.
***THIS PROJECT IS NOT SO MUCH ABOUT DESIGN BUT ABOUT FUNCTIONALITY OF THE APPLICATION. IT MUST HAVE THE FEATURES I HAVE ASKED FOR THAT WORK TOGETHER. I AM WILLING TO PAY A LITTLE MORE AS A BONUS IF YOU CAN ACCOMPLISH THIS. ALSO IF I FIN THE RIGHT PERSON THAT CAN DO THIS I WILL MAKE IT A GUARNTEED PROJECT.

- Functionality and Track and record all the info we need

```html
<!DOCTYPE html>
<html lang="en">
<head>
<meta charset="utf-8">
<title>Forma Studio – Check-in Demo Preview</title>
<link href="https://fonts.googleapis.com/css2?family=Inter:wght@400;500;600;700&family=Noto+Sans:wght@400;700&display=swap" rel="stylesheet">
<style>
:root{
  --page:#efefef;
  --ink:#111111;
  --navy:#0f1b2d;
  --muted:#6b7280;
  --line:#e5e7eb;
  --blue:#1570ef;
  --indigo:#4f46e5;
  --violet:#5b3df5;
  --green:#16a34a;
  --green-bg:#ecfdf3;
  --blue-bg:#eaf2fe;
  --pink:#d946ef;
  --pink-bg:#fbf1fd;
  --screen:#f7f9fc;
  --white:#ffffff;
  --brand:#e2530f;
}
*{box-sizing:border-box;margin:0;padding:0}
html,body{width:1200px;height:931px;overflow:hidden;background:var(--page)}
body{position:relative;font-family:"Inter",sans-serif;color:var(--navy)}

.message{position:absolute;left:15px;top:10px;width:1070px;font-family:"Noto Sans",sans-serif;font-size:18.3px;line-height:21.5px;color:var(--ink)}
.message p{margin-bottom:21.5px}
.message b{font-weight:700}

/* ---------- tablet screen ---------- */
.tablet{position:absolute;left:129px;top:357px;width:679px;height:503px;background:var(--screen);border-radius:6px;overflow:hidden;box-shadow:0 6px 24px rgba(0,0,0,.12)}
.abs{position:absolute}
.sidebar{position:absolute;left:0;top:0;width:188px;height:503px;background:var(--white);border-right:1px solid var(--line)}
.brand{font-weight:700;color:var(--navy);letter-spacing:.3px}
.brand-dot{display:inline-block;width:8px;height:8px;background:var(--brand);border-radius:50%;margin-right:5px;vertical-align:middle}
.side-brand{position:absolute;left:0;width:188px;top:22px;text-align:center;font-size:19px}
.side-tag{position:absolute;left:0;width:188px;top:66px;text-align:center;font-size:8.5px;color:#4b5563}
.side-rule{position:absolute;left:0;top:88px;width:188px;height:1px;background:var(--line)}
.nav{position:absolute;left:14px;width:164px;border-radius:9px;display:flex;align-items:flex-start;gap:9px;padding:10px 9px}
.nav-active{top:103px;height:56px;background:linear-gradient(90deg,var(--blue),var(--violet));color:#fff;box-shadow:0 4px 10px rgba(79,70,229,.3)}
.nav-icon{flex:none;width:21px;height:21px;border-radius:50%;display:flex;align-items:center;justify-content:center}
.nav-title{font-size:8.5px;font-weight:600}
.nav-sub{font-size:7px;line-height:11px;margin-top:3px;opacity:.85}
.nav-plain .nav-title{color:var(--navy);font-weight:500}
.nav-plain .nav-sub{color:var(--muted);opacity:1}
.side-stat{position:absolute;left:14px;top:443px;width:164px;height:51px;background:var(--green-bg);border:1px solid #c9f0d8;border-radius:9px;padding:9px}
.side-stat .lbl{font-size:8px;color:var(--green);font-weight:500}
.side-stat .num{font-size:14px;font-weight:700;color:#064e3b;margin-top:3px}
.side-stat .ico{position:absolute;right:9px;top:15px;width:21px;height:21px;border-radius:50%;background:#c8f1d9;display:flex;align-items:center;justify-content:center}

.header{position:absolute;left:188px;top:0;width:491px;height:88px;background:var(--white);border-bottom:1px solid var(--line)}
.h-title{position:absolute;left:14px;top:28px;font-size:14px;font-weight:600}
.h-date{position:absolute;left:14px;top:51px;font-size:9.5px;color:#4b5563}
.h-brand{position:absolute;left:299px;top:38px;font-size:15px}
.h-card{position:absolute;left:380px;top:20px;width:99px;height:53px;background:var(--blue-bg);border:1px solid #d4e4fb;border-radius:9px;padding:10px 9px 0 37px}
.h-card .ico{position:absolute;left:10px;top:16px}
.h-card .lbl{font-size:8px;color:var(--blue)}
.h-card .num{font-size:12.5px;font-weight:700;color:#103d8a;margin-top:2px}

.stat{position:absolute;top:103px;width:149px;height:56px;border-radius:9px;padding:11px 0 0 37px}
.stat .ico{position:absolute;left:9px;top:15px;width:21px;height:21px;border-radius:50%;display:flex;align-items:center;justify-content:center}
.stat .lbl{font-size:8px;font-weight:500}
.stat .num{font-size:14px;font-weight:700;margin-top:3px}
.stat-blue{left:202px;background:var(--blue-bg);border:1px solid #d8e6fb}
.stat-blue .ico{background:var(--blue)}
.stat-blue .lbl{color:var(--blue)}.stat-blue .num{color:#103d8a}
.stat-green{left:360px;background:var(--green-bg);border:1px solid #cdeedc}
.stat-green .ico{background:var(--green)}
.stat-green .lbl{color:var(--green)}.stat-green .num{color:#064e3b}
.stat-pink{left:518px;background:var(--pink-bg);border:1px solid #f2dcf7}
.stat-pink .ico{background:var(--pink)}
.stat-pink .lbl{color:#a21caf}.stat-pink .num{color:#6b1479}

.form{position:absolute;left:202px;top:176px;width:465px;height:217px;background:var(--white);border:1px solid #eceef2;border-radius:10px;box-shadow:0 2px 8px rgba(15,27,45,.05)}
.form-title{position:absolute;left:14px;top:14px;font-size:9.5px;font-weight:500;display:flex;align-items:center;gap:6px}
.label{position:absolute;font-size:8.3px;color:#374151;font-weight:500}
.field{position:absolute;height:29px;border:1px solid #d9dde3;border-radius:6px;font-size:8.5px;color:var(--muted);display:flex;align-items:center;padding:0 8px;gap:6px}
.select{height:21px;font-size:9px;justify-content:space-between}
.cta{position:absolute;left:14px;top:169px;width:437px;height:33px;border-radius:6px;background:linear-gradient(90deg,#0b74ff,var(--violet));color:#fff;font-size:10px;font-weight:600;display:flex;align-items:center;justify-content:center;gap:8px;box-shadow:0 4px 10px rgba(79,70,229,.25)}

/* ---------- phone screen ---------- */
.phone{position:absolute;left:887px;top:393px;width:193px;height:417px;background:#f3f5f8;border-radius:14px;overflow:hidden;box-shadow:0 6px 20px rgba(0,0,0,.12)}
.p-top{position:absolute;left:0;top:0;width:193px;height:58px;background:var(--white);border-bottom:1px solid var(--line)}
.p-brand{position:absolute;left:7px;top:15px;font-size:9px}
.p-tag{position:absolute;left:57px;top:18px;font-size:4.5px;color:var(--muted)}
.p-badge{position:absolute;left:139px;top:16px;width:48px;height:10px;border-radius:5px;background:#dcfce7;color:var(--green);font-size:4.3px;font-weight:600;display:flex;align-items:center;justify-content:center}
.p-tabs{position:absolute;left:7px;top:36px;display:flex;gap:5px;font-size:5px;color:#374151}
.p-tab{height:13px;padding:0 6px;border-radius:7px;display:flex;align-items:center;gap:3px}
.p-tab-active{background:var(--blue);color:#fff}
.p-hero-icon{position:absolute;left:86px;top:66px;width:22px;height:22px;border-radius:6px;background:#16a34a;display:flex;align-items:center;justify-content:center}
.p-hero-title{position:absolute;left:0;top:92px;width:193px;text-align:center;font-size:7.5px;font-weight:600}
.p-hero-sub{position:absolute;left:0;top:107px;width:193px;text-align:center;font-size:5.3px;color:#4b5563}
.p-type{position:absolute;width:87px;height:39px;background:var(--white);border-radius:6px;border:1px solid #eef0f3;text-align:center;font-size:5px;font-weight:500;padding-top:8px}
.p-type .dot{width:7px;height:7px;margin:0 auto 5px;border-radius:2px}
.p-card{position:absolute;left:7px;top:220px;width:180px;height:210px;background:var(--white);border-radius:7px;border:1px solid #eef0f3}
.p-card-title{position:absolute;left:9px;top:10px;font-size:5.8px;display:flex;gap:4px;align-items:center}
.p-label{position:absolute;left:9px;font-size:4.8px;font-weight:500;color:#374151}
.p-field{position:absolute;left:9px;width:162px;height:18px;border:1px solid #e1e4e8;border-radius:4px;font-size:5.3px;color:var(--muted);display:flex;align-items:center;padding:0 5px;gap:3px}
</style>
</head>
<body>

<div class="message">
  <p>I have&nbsp; created a (non-100% ready but still functional) <b>live demo</b> of your request. It should give you an idea of how the end-product will be</p>
  <p>Check it out here: <b>https://shortly.link/forma-gym-demo</b></p>
  <p>What you will see is a rough demo just for previewing purposes. It’s all created locally and all components are packed. It will be properly and more professionally developed / bug-tested when you approve of this first demo. I think I will need another 5-6 days to properly implement it using client DB, Backups, Safety, Bug killing, etc.</p>
  <p>I wanted you to have a look and feel of what you asked for. With respect to your request that primarily you want something that WORKS.</p>
  <p style="margin:0">For Check-in try this Example:<br>Check-in <b>Dana Whitfield</b> with Trainer: <b>Marco Reyes</b> for a <b>Single</b> Session Type</p>
</div>

<!-- Tablet check-in screen -->
<section class="tablet" aria-label="Check-in screen">
  <aside class="sidebar">
    <div class="side-brand brand"><span class="brand-dot"></span>FORMA</div>
    <div class="side-tag">Training Management</div>
    <div class="side-rule"></div>

    <div class="nav nav-active">
      <span class="nav-icon" style="background:rgba(255,255,255,.22)">
        <svg width="12" height="12" viewBox="0 0 24 24" fill="none" stroke="#fff" stroke-width="2.4"><circle cx="12" cy="12" r="9"/><path d="M8 12l3 3 5-6"/></svg>
      </span>
      <div><div class="nav-title">Check-in</div><div class="nav-sub">Client check-in and session management</div></div>
    </div>
    <div class="nav nav-plain" style="top:170px">
      <span class="nav-icon" style="background:var(--blue)">
        <svg width="11" height="11" viewBox="0 0 24 24" fill="none" stroke="#fff" stroke-width="2.4"><circle cx="9" cy="8" r="4"/><path d="M2 21c0-4 3-7 7-7s7 3 7 7M19 8v6M16 11h6"/></svg>
      </span>
      <div><div class="nav-title">Add Client</div><div class="nav-sub">Register new clients</div></div>
    </div>
    <div class="nav nav-plain" style="top:220px">
      <span class="nav-icon" style="background:var(--pink)">
        <svg width="11" height="11" viewBox="0 0 24 24" fill="none" stroke="#fff" stroke-width="2.4"><circle cx="12" cy="12" r="3"/><circle cx="12" cy="12" r="8" stroke-dasharray="3 2.3"/></svg>
      </span>
      <div><div class="nav-title">Admin Panel</div><div class="nav-sub">Administrative functions</div></div>
    </div>

    <div class="side-stat">
      <div class="lbl">Today's Sessions</div>
      <div class="num">12</div>
      <span class="ico"><svg width="10" height="10" viewBox="0 0 24 24" fill="none" stroke="#16a34a" stroke-width="2.6"><path d="M3 3v18h18M8 17v-6M13 17V7M18 17v-9"/></svg></span>
    </div>
  </aside>

  <header class="header">
    <div class="h-title">Check-in</div>
    <div class="h-date">Sunday, June 29, 2025</div>
    <div class="h-brand brand">FORMA</div>
    <div class="h-card">
      <svg class="ico" width="14" height="14" viewBox="0 0 24 24" fill="none" stroke="#1570ef" stroke-width="2"><circle cx="9" cy="8" r="4"/><path d="M2 21c0-4 3-7 7-7s7 3 7 7M16 4a4 4 0 010 8M22 21c0-3-2-6-5-7"/></svg>
      <div class="lbl">Active Clients</div>
      <div class="num">247</div>
    </div>
  </header>

  <div class="stat stat-blue">
    <span class="ico"><svg width="11" height="11" viewBox="0 0 24 24" fill="none" stroke="#fff" stroke-width="2.4"><circle cx="9" cy="8" r="4"/><path d="M2 21c0-4 3-7 7-7s7 3 7 7M16 4a4 4 0 010 8"/></svg></span>
    <div class="lbl">Total Clients</div><div class="num">6</div>
  </div>
  <div class="stat stat-green">
    <span class="ico"><svg width="11" height="11" viewBox="0 0 24 24" fill="none" stroke="#fff" stroke-width="2.4"><circle cx="12" cy="12" r="9"/><path d="M12 7v5l3 2"/></svg></span>
    <div class="lbl">Today's Sessions</div><div class="num">12</div>
  </div>
  <div class="stat stat-pink">
    <span class="ico"><svg width="11" height="11" viewBox="0 0 24 24" fill="none" stroke="#fff" stroke-width="2.4"><path d="M13 2L4 14h7l-1 8 9-12h-7z"/></svg></span>
    <div class="lbl">Active Now</div><div class="num">4</div>
  </div>

  <div class="form">
    <div class="form-title">
      <svg width="13" height="13" viewBox="0 0 24 24" fill="none" stroke="#1570ef" stroke-width="2.2"><circle cx="12" cy="12" r="9"/><path d="M8 12l3 3 5-6"/></svg>
      Client Check-in
    </div>
    <div class="label" style="left:14px;top:56px">Client Name</div>
    <div class="field" style="left:14px;top:70px;width:437px">
      <svg width="10" height="10" viewBox="0 0 24 24" fill="none" stroke="#6b7280" stroke-width="2.2"><circle cx="11" cy="11" r="7"/><path d="M21 21l-5-5"/></svg>
      Start typing client name...
    </div>
    <div class="label" style="left:14px;top:113px">Trainer Name</div>
    <div class="field select" style="left:14px;top:127px;width:211px">Select trainer...
      <svg width="8" height="8" viewBox="0 0 24 24" fill="none" stroke="#6b7280" stroke-width="2.4"><path d="M6 9l6 6 6-6"/></svg></div>
    <div class="label" style="left:239px;top:113px">Session Type</div>
    <div class="field select" style="left:239px;top:127px;width:212px">Select session type...
      <svg width="8" height="8" viewBox="0 0 24 24" fill="none" stroke="#6b7280" stroke-width="2.4"><path d="M6 9l6 6 6-6"/></svg></div>
    <div class="cta">
      <svg width="11" height="11" viewBox="0 0 24 24" fill="none" stroke="#fff" stroke-width="2.4"><circle cx="12" cy="12" r="9"/><path d="M8 12l3 3 5-6"/></svg>
      Check In Client
    </div>
  </div>
</section>

<!-- Phone add-client screen -->
<section class="phone" aria-label="Add client screen">
  <div class="p-top">
    <div class="p-brand brand"><span class="brand-dot" style="width:5px;height:5px;margin-right:3px"></span>FORMA</div>
    <div class="p-tag">Training Management</div>
    <div class="p-badge">12 Sessions Today</div>
    <div class="p-tabs">
      <span class="p-tab">✓ Check-in</span>
      <span class="p-tab p-tab-active">+ Add Client</span>
      <span class="p-tab">⚙ Admin Panel</span>
    </div>
  </div>

  <div class="p-hero-icon"><svg width="12" height="12" viewBox="0 0 24 24" fill="none" stroke="#fff" stroke-width="2.2"><circle cx="9" cy="8" r="4"/><path d="M2 21c0-4 3-7 7-7s7 3 7 7M19 8v6M16 11h6"/></svg></div>
  <div class="p-hero-title">Add New Client</div>
  <div class="p-hero-sub">Register a new client and set up their training package</div>

  <div class="p-type" style="left:7px;top:125px"><div class="dot" style="background:#6d28d9;border-radius:50%"></div>Single</div>
  <div class="p-type" style="left:100px;top:125px"><div class="dot" style="background:#6d28d9;width:10px"></div>Partner</div>
  <div class="p-type" style="left:7px;top:170px"><div class="dot" style="background:#f97316"></div>Drop-In</div>
  <div class="p-type" style="left:100px;top:170px"><div class="dot" style="background:#2563eb"></div>Group</div>

  <div class="p-card">
    <div class="p-card-title"><svg width="7" height="7" viewBox="0 0 24 24" fill="none" stroke="#16a34a" stroke-width="2.6"><circle cx="9" cy="8" r="4"/><path d="M2 21c0-4 3-7 7-7s7 3 7 7"/></svg>Client Information</div>
    <div class="p-label" style="top:35px">First Name</div>
    <div class="p-field" style="top:44px">First name</div>
    <div class="p-label" style="top:70px">Last Name</div>
    <div class="p-field" style="top:78px">Last name</div>
    <div class="p-label" style="top:106px">Email Address</div>
    <div class="p-field" style="top:115px">✉ client@example.com</div>
    <div class="p-label" style="top:140px">Phone Number</div>
    <div class="p-field" style="top:149px">☏ (555) 123-4567</div>
    <div class="p-label" style="top:177px">Starting Session Count</div>
    <div class="p-field" style="top:185px"># Enter number of sessions</div>
  </div>
</section>

</body>
</html>
```